Basketball Training Facility Flyer Design

We need a killer flyer designed for our brand new state of the art basketball training facility here in Syracuse, Utah. This flyer will be distributed to coaches, parents and players in a large school district in Davis and Weber county, Utah. The purpose of the flyer is to announce the launch of the new facility and to encourage parents, coaches and players to come and try out the facility for a free initial session. We're offering a completely complimentary first training session to introduce customers to the facility at no cost.

We use technology and equipment that is typically found in PLQ-level training facilities and gymnasiums. Our website can be found here for some additional information - www.crestcourthoops.net. Customers can easily book and pay online through our website (the functionality will be done by the time we distribute the completed flyer).

The design needs to highlight the equipment we offer at the facility, because no other basketball training center has the same level of technology we do. We want the flyer to be clean and simple.

Please see must haves for specific details.

The size of the flyer we want to print is 5.75 inches by 9.5 inches.

Target Market(s)

Parents of basketball players of all skill levels age 8-18.

Industry/Entity Type

Training

Requirements
Must have
• Design must include this header: You want to dominate on the court. We have the formula to make that happen.

Design must include this sub header or highlight: Free Introductory Training Session!

The design must include our Logo

The design must include the photos attached of the Ravel, the Liftorra and the 37Twelve

Under the the photo of the Ravel 5200 (attached) please include this verbiage:
Game Shots in Game Spots at Game Speed

Under the photo of the Liftorra (see attached) please include this verbiage:
Improve Power, Agility and Speed like Never Before

Under the photo of the 37Twelve (attached) please include this verbiage:
Real Time Statistics to Improve Dribble Speed, Accuracy and Right / Left Comparison

Include this verbiage somewhere in the design: Technology Used by PLQ and the Best D-1 College Teams

The design must include a strong call to action: Call or Click Now to Schedule A Free Training Session!

The design must include our contact information in easy-to-read font and size (also specifically highlighting the website):

Schedule Online in Less Than 60 Seconds!
Call or Click
801-574-2918
www.crestcourthoops.net
Nice to have
• For examples of the type of design we like, please see the attached images labeled

Please use stock photos of your preference to go in the flyer (preferably images of youth basketball training or kids in basketball training)

We don't want the flyer to be too cluttered, so please use images at your discretion.

Thank you!

```html
<!DOCTYPE html>
<html lang="en">
<head>
<meta charset="utf-8">
<title>Crest Court Academy – Free Training Session Flyer</title>
<link href="https://fonts.googleapis.com/css2?family=Bebas+Neue&family=Oswald:wght@500;600&family=Open+Sans:wght@600;700;800&display=swap" rel="stylesheet">
<style>
  :root {
    --orange: #f7941d;
    --orange-deep: #e8731a;
    --red: #9b2b23;
    --red-dark: #7d1f1a;
    --ink: #1f1f1f;
    --grey-light: #d9d9d9;
    --grey-mid: #9a9a9a;
    --white: #ffffff;
    --page: #ececec;
  }
  * { box-sizing: border-box; margin: 0; padding: 0; }
  html, body { width: 949px; height: 1200px; overflow: hidden; background: var(--page); }
  .flyer {
    position: absolute; left: 128px; top: 30px;
    width: 577px; height: 950px;
    transform: scale(1.2); transform-origin: 0 0;
    background: var(--white); overflow: hidden;
    box-shadow: 0 4px 14px rgba(0,0,0,.25);
    font-family: "Open Sans", Arial, sans-serif;
  }
  .abs { position: absolute; }

  /* hero */
  .hero-photo {
    left: 0; top: 70px; width: 577px; height: 350px;
    background: linear-gradient(160deg, #f0f0f0 0%, #bdbdbd 45%, #8a8a8a 100%);
  }
  .athlete-photo {
    left: 335px; top: 0; width: 242px; height: 420px;
    background: radial-gradient(ellipse at 50% 55%, #b5402f 0%, #7a2a22 35%, rgba(60,40,35,.85) 60%, rgba(60,40,35,0) 75%);
  }
  .top-swoosh { left: 0; top: 0; width: 577px; height: 140px; }
  .brand {
    left: 114px; top: 4px; width: 116px; height: 116px; border-radius: 50%;
    background: var(--orange-deep); border: 4px solid var(--white);
    display: flex; align-items: center; justify-content: center; text-align: center;
    font-family: "Oswald", sans-serif; font-weight: 600; font-size: 17px; line-height: 1.05;
    color: var(--white); letter-spacing: .5px;
  }
  .headline { left: 10px; top: 134px; width: 340px; text-align: center; font-family: "Bebas Neue", sans-serif; line-height: .92; font-weight: 400; }
  .headline .lead, .headline .tail { color: var(--white); font-size: 64px; text-shadow: 2px 2px 0 #555, 0 0 6px rgba(0,0,0,.4); }
  .headline .lead { font-size: 60px; }
  .headline .key { color: var(--orange); font-size: 112px; text-shadow: 2px 2px 0 #7a3d0a; }
  .formula {
    left: 10px; top: 360px; width: 340px; text-align: center;
    font-family: "Open Sans", sans-serif; font-weight: 800; font-size: 17px; line-height: 1.25;
    color: var(--orange); letter-spacing: -.6px; text-transform: uppercase;
    text-shadow: 1px 1px 0 #6b3a0a;
  }

  /* technology band */
  .tech-band {
    left: 0; top: 418px; width: 577px; height: 52px; background: var(--red);
    display: flex; align-items: center; justify-content: center;
    font-family: "Bebas Neue", sans-serif; font-size: 37px; color: var(--white); letter-spacing: .5px;
    white-space: nowrap;
  }
  .gear { top: 474px; height: 136px; border-radius: 4px; }
  .gear-ball { left: 30px; width: 150px; background: radial-gradient(circle at 40% 45%, #d77a3a 0%, #a44a1e 55%, #fff 75%); }
  .gear-platform { left: 218px; width: 150px; background: linear-gradient(170deg, #fff 0%, #9fb4d6 45%, #2f5fb0 70%, #fff 100%); }
  .gear-rebounder { left: 420px; width: 120px; background: linear-gradient(180deg, #f1f1f1 0%, #e0e0e0 40%, #c23a2b 70%, #fff 100%); }

  .spec-band { left: 0; top: 612px; width: 577px; height: 70px; background: var(--ink); }
  .specs { display: flex; justify-content: space-around; padding: 4px 6px 0; }
  .spec {
    width: 180px; text-align: center; color: var(--white);
    font-family: "Oswald", sans-serif; font-weight: 500; font-size: 7.2px; line-height: 1.35; text-transform: uppercase;
  }
  .pro-line {
    margin-top: 8px; text-align: center; color: var(--orange);
    font-weight: 700; font-size: 16.5px; letter-spacing: -.2px; white-space: nowrap;
  }

  /* call to action */
  .cta {
    left: 0; top: 698px; width: 577px; text-align: center; white-space: nowrap;
    font-family: "Bebas Neue", sans-serif; font-weight: 400; font-size: 31px; line-height: 1.1;
    color: var(--red); letter-spacing: .3px;
  }
  .contact { left: 14px; top: 766px; width: 330px; }
  .contact .note { font-weight: 700; font-size: 13px; color: var(--ink); white-space: nowrap; }
  .contact .web { font-weight: 700; font-size: 19.5px; color: var(--red); margin-top: 4px; white-space: nowrap; }
  .contact .phone { font-family: "Oswald", sans-serif; font-weight: 500; font-size: 52px; color: var(--ink); line-height: 1.1; letter-spacing: 1px; white-space: nowrap; }
  .offer { left: 350px; top: 762px; width: 220px; }
  .offer .ages { font-family: "Oswald", sans-serif; font-weight: 500; font-size: 21px; color: var(--red); white-space: nowrap; }
  .offer ul { list-style: none; margin-top: 6px; }
  .offer li { position: relative; padding-left: 17px; font-size: 11px; line-height: 1.35; color: #333; font-weight: 600; }
  .offer li.group { color: var(--red); font-weight: 800; }
  .offer li svg { position: absolute; left: 0; top: 2px; width: 13px; height: 12px; }

  .footer-band {
    left: 0; top: 915px; width: 577px; height: 35px; background: var(--orange);
    display: flex; align-items: center; justify-content: center;
    color: var(--white); font-weight: 700; font-size: 15.5px; white-space: nowrap;
  }
</style>
</head>
<body>
<div class="flyer">
  <div class="abs hero-photo" role="img" aria-label="Greyscale photo of a young player training in a gym"></div>
  <div class="abs athlete-photo" role="img" aria-label="Cut-out photo of a basketball player in red shorts dunking"></div>

  <svg class="abs top-swoosh" viewBox="0 0 577 140" aria-hidden="true">
    <path d="M0 0 H577 V20 C430 10 300 40 180 70 C110 88 50 100 0 104 Z" fill="#ffffff"/>
    <path d="M0 0 H577 V10 C420 6 300 26 180 52 C110 68 50 80 0 84 Z" fill="#f7941d"/>
    <path d="M0 0 H577 V4 C420 0 300 14 180 36 C110 50 50 60 0 62 Z" fill="#ffffff"/>
    <path d="M0 100 C60 96 120 84 190 66 C300 38 430 18 577 22 V34 C430 30 300 52 190 80 C120 98 60 108 0 112 Z" fill="#9b2b23"/>
    <path d="M0 112 C60 108 120 98 190 80 C300 52 430 30 577 34 V40 C430 38 300 60 190 90 C120 108 60 118 0 122 Z" fill="#f7941d"/>
  </svg>

  <div class="abs brand">CREST<br>COURT<br>ACADEMY</div>

  <h1 class="abs headline">
    <span class="lead">You want to</span><br>
    <span class="key">Dominate</span><br>
    <span class="tail">On the court</span>
  </h1>
  <p class="abs formula">We have the formula to<br>make that happen</p>

  <div class="abs tech-band">Superior Technology = Superior Training</div>

  <div class="abs gear gear-ball" role="img" aria-label="Photo of the 37Twelve smart basketball with a phone showing stats"></div>
  <div class="abs gear gear-platform" role="img" aria-label="Photo of a player training on the Liftorra resistance platform"></div>
  <div class="abs gear gear-rebounder" role="img" aria-label="Photo of the Ravel 5200 shooting machine"></div>

  <div class="abs spec-band">
    <div class="specs">
      <p class="spec">Real time statistics to improve dribble speed, accuracy and right / left comparison</p>
      <p class="spec">Speed, power &amp; vertical jump<br>Game shots in game spots at game speed</p>
      <p class="spec">1,800 shots an hour!<br>Improve power, agility and speed like never before</p>
    </div>
    <p class="pro-line">Technology Used by PLQ and the Best D-1 College Teams</p>
  </div>

  <h2 class="abs cta">Call now to schedule a free training session!</h2>

  <div class="abs contact">
    <p class="note">Schedule Online in Less Than 60 Seconds!</p>
    <p class="web">www.crestcourthoops.net</p>
    <p class="phone">801-574-2918</p>
  </div>

  <div class="abs offer">
    <p class="ages">Ages 6+, Boys and Girls</p>
    <ul>
      <li><svg viewBox="0 0 24 23"><path d="M12 0l3.5 7.6 8.3.9-6.2 5.6 1.8 8.2L12 18.1 4.6 22.3l1.8-8.2L.2 8.5l8.3-.9z" fill="#f7941d"/></svg>One on One / Individual Sessions</li>
      <li class="group"><svg viewBox="0 0 24 23"><path d="M12 0l3.5 7.6 8.3.9-6.2 5.6 1.8 8.2L12 18.1 4.6 22.3l1.8-8.2L.2 8.5l8.3-.9z" fill="#f7941d"/></svg>Group Sessions (2-5 players with discounts applying)</li>
      <li><svg viewBox="0 0 24 23"><path d="M12 0l3.5 7.6 8.3.9-6.2 5.6 1.8 8.2L12 18.1 4.6 22.3l1.8-8.2L.2 8.5l8.3-.9z" fill="#f7941d"/></svg>Team Training</li>
      <li><svg viewBox="0 0 24 23"><path d="M12 0l3.5 7.6 8.3.9-6.2 5.6 1.8 8.2L12 18.1 4.6 22.3l1.8-8.2L.2 8.5l8.3-.9z" fill="#f7941d"/></svg>Monthly Memberships</li>
    </ul>
  </div>

  <div class="abs footer-band">The Only Basketball Training Facility of its Kind in Utah</div>
</div>
</body>
</html>
```